BrivoMatex. Lantern for the Steady Growth. Business card

Professional business card for BrivoMatex (Lantern for the Steady Growth)
My rationale: Strategy-> Execution-> Results-> Value that lead to the BrivoMatex name: We put the Lantern for the Steady Growth.
We deliver value to our customers helping them at defining a good strategy (cyan arrow). 90% of well formulated strategies fail due to poor execution so we also consider strategical execution very important (green arrow). Due to the execution we obtain the results (blue arrow). Finally, the results provide feedback to redefine strategy, and the new strategy has to be executed and new results obtained providing new feedback and on and on. It's like a wheel that finally, must create corporate value: value for shareholders, staholders, employees, providers...-

Target Market(s)

CEOs and steering comitees , invewrnent funds

Industry/Entity Type

Business Consultant

Contact Information for Business Card

Tommaso Ferlini
CEO & Founder
tommaso.ferlini@brivomatex.example
Mobile: +34 611.205.938
www.brivomatex.example

Colors

Designer to choose colors to be used in the design.

Requirements
Nice to have
• Nice to hace the words: Strategy, execution, results
• Nice to vave the claim: Lantern for the Steady Growth
• The three colors should be shown:
• cyan for STRATEGY
• green for EXECUTION
• blue for RESULTS
Should not have
• Complete black background

```html
<!DOCTYPE html>
<html lang="en">
<head>
<meta charset="utf-8">
<title>BrivoMatex — Business Card</title>
<link href="https://fonts.googleapis.com/css2?family=Source+Sans+3:wght@400;600;700;800&display=swap" rel="stylesheet">
<style>
  :root {
    --blue: #1f3c8f;
    --green: #8dc63f;
    --cyan: #27a9e1;
    --paper: #ffffff;
    --backdrop: #c9cbce;
    --shadow: rgba(0, 0, 0, 0.22);
  }
  * { box-sizing: border-box; margin: 0; padding: 0; }
  html, body {
    width: 1200px;
    height: 800px;
    overflow: hidden;
  }
  body {
    background: var(--backdrop);
    font-family: "Source Sans 3", "Helvetica Neue", Arial, sans-serif;
    color: var(--blue);
    display: flex;
    flex-direction: column;
    align-items: center;
    justify-content: center;
    gap: 44px;
  }
  .card {
    position: relative;
    width: 580px;
    height: 330px;
    background: var(--paper);
    box-shadow: 0 8px 22px var(--shadow);
    overflow: hidden;
  }

  /* Front side */
  .pillars {
    position: absolute;
    left: 58px;
    top: 66px;
    display: flex;
    flex-direction: column;
    gap: 8px;
    font-weight: 700;
    font-size: 30px;
    letter-spacing: 0.2em;
    line-height: 1;
  }
  .pillar--results { color: var(--blue); }
  .pillar--execution { color: var(--green); }
  .pillar--strategy { color: var(--cyan); }

  .front-brand {
    position: absolute;
    right: 42px;
    bottom: 44px;
    text-align: right;
  }
  .brand-name {
    font-weight: 800;
    color: var(--blue);
    letter-spacing: -0.02em;
    line-height: 1;
  }
  .front-brand .brand-name { font-size: 50px; }
  .tagline {
    margin-top: 6px;
    font-size: 15px;
    font-weight: 700;
    letter-spacing: 0.03em;
    text-transform: uppercase;
    color: var(--blue);
  }

  /* Back side */
  .edge-band {
    position: absolute;
    left: 0;
    top: 0;
    width: 16px;
    height: 100%;
    display: flex;
    flex-direction: column;
  }
  .edge-band span { flex: 1; }
  .edge-band .band-blue { background: var(--blue); }
  .edge-band .band-green { background: var(--green); }
  .edge-band .band-cyan { background: var(--cyan); }

  .back-brand {
    position: absolute;
    right: 58px;
    top: 120px;
  }
  .back-brand .brand-name { font-size: 52px; }

  .contact {
    position: absolute;
    left: 56px;
    bottom: 46px;
  }
  .person-name {
    font-size: 22px;
    font-weight: 700;
    color: var(--blue);
    line-height: 1.1;
  }
  .person-role {
    font-size: 16px;
    color: var(--cyan);
    margin-bottom: 14px;
  }
  .contact-list { list-style: none; }
  .contact-list li {
    display: flex;
    align-items: center;
    gap: 8px;
    font-size: 16px;
    line-height: 1.4;
    color: var(--blue);
  }
  .contact-list svg {
    width: 14px;
    height: 14px;
    flex: none;
    stroke: var(--green);
    fill: none;
    stroke-width: 1.6;
  }
</style>
</head>
<body>

  <section class="card card--front" aria-label="Business card front">
    <div class="pillars">
      <span class="pillar pillar--results">RESULTS</span>
      <span class="pillar pillar--execution">EXECUTION</span>
      <span class="pillar pillar--strategy">STRATEGY</span>
    </div>
    <div class="front-brand">
      <div class="brand-name">BrivoMatex</div>
      <div class="tagline">Lantern for the Steady Growth</div>
    </div>
  </section>

  <section class="card card--back" aria-label="Business card back">
    <div class="edge-band" aria-hidden="true">
      <span class="band-blue"></span>
      <span class="band-green"></span>
      <span class="band-cyan"></span>
    </div>

    <div class="back-brand">
      <div class="brand-name">BrivoMatex</div>
    </div>

    <div class="contact">
      <div class="person-name">Tommaso Ferlini</div>
      <div class="person-role">CEO &amp; Founder</div>
      <ul class="contact-list">
        <li>
          <svg viewBox="0 0 14 14" aria-hidden="true"><rect x="3.5" y="1" width="7" height="12" rx="1.2"/><line x1="6" y1="11" x2="8" y2="11"/></svg>
          +34 611.205.938
        </li>
        <li>
          <svg viewBox="0 0 14 14" aria-hidden="true"><rect x="1" y="3" width="12" height="8"/><polyline points="1,3 7,8 13,3"/></svg>
          tommaso.ferlini@brivomatex.example
        </li>
        <li>
          <svg viewBox="0 0 14 14" aria-hidden="true"><circle cx="7" cy="7" r="5.8"/><ellipse cx="7" cy="7" rx="2.6" ry="5.8"/><line x1="1.2" y1="7" x2="12.8" y2="7"/></svg>
          www.brivomatex.example
        </li>
      </ul>
    </div>
  </section>

</body>
</html>
```